Capability Statement Flyer

We want to develop a flyer to show potential clients our work capability. We want to incorporate our logo. You can reference our website for any other graphics you may want to incorporate. Our blue CMYK is 100-80-0-22

Colors
0555a3

Requirements
Must have
• Capability Statement
• Our expertise and technical resources fuel the delivery of our services. As a leading provider of construction services, Tallmere Construction focuses on providing solutions for civil infrastructure, industrial infrastructure, and commercial market segments. Driven by a commitment to continuous improvement, Tallmere Construction has the expertise in the following key areas:
• • Design Build/Problem Solving
• • Storm and Process Water Systems
• • Heavy and Structural Concrete
• • Bridge Construction
• • Building Construction and Restoration
• • Hardscapes
• • All Civil Construction and Utility
Nice to have
• Creativity to present to potential clients. Not just words on the page

```html
<!DOCTYPE html>
<html lang="en">
<head>
<meta charset="utf-8">
<title>Tallmere Construction – Capability Statement</title>
<link href="https://fonts.googleapis.com/css2?family=Montserrat:wght@500;700&family=Jost:wght@400&display=swap" rel="stylesheet">
<style>
  :root {
    --brand-blue: #22397f;
    --charcoal: #3d3d3d;
    --ink: #1e1e1e;
    --paper: #ffffff;
    --backdrop: #a9a9a9;
  }
  * { margin: 0; padding: 0; box-sizing: border-box; }
  html, body { width: 849px; height: 1200px; overflow: hidden; background: var(--backdrop); }
  .flyer { position: relative; width: 849px; height: 1200px; }
  .sheet { position: absolute; left: 13px; top: 18px; width: 822px; height: 1163px; background: var(--paper); }
  .abs { position: absolute; }

  .brand { left: 48px; top: 44px; display: flex; align-items: center; gap: 10px; }
  .brand-square { width: 58px; height: 58px; background: var(--brand-blue); }
  .brand-name { font-family: "Montserrat", sans-serif; font-weight: 700; color: var(--brand-blue);
    font-size: 22px; line-height: 1.05; letter-spacing: 1px; text-transform: uppercase; }

  .web { right: 51px; top: 62px; font-family: "Montserrat", sans-serif; font-weight: 500; font-size: 21px; color: var(--ink); }
  .web span { color: var(--brand-blue); }

  .hero-band { left: 13px; top: 130px; width: 787px; height: 480px; background: var(--brand-blue); }
  .hero-shadow { left: 48px; top: 166px; width: 787px; height: 480px; background: var(--charcoal); }
  .hero-photo { left: 48px; top: 166px; width: 752px; height: 444px;
    background: linear-gradient(180deg, #9cc4e6 0%, #dfe9f1 40%, #c9b9a6 58%, #7c8a6d 80%, #6e9a46 100%); }

  .section-title { font-family: "Montserrat", sans-serif; font-weight: 700; font-size: 18px; letter-spacing: 0.5px;
    color: var(--ink); padding-bottom: 3px; border-bottom: 1.5px solid var(--charcoal); }
  .section-title .lead { color: var(--brand-blue); }

  .services-title { left: 48px; top: 669px; }
  .services-intro { left: 48px; top: 702px; width: 380px; font-family: "Jost", sans-serif; font-size: 15px; line-height: 20px; color: var(--ink); }

  .service-list { left: 50px; top: 854px; list-style: none; }
  .service-list li { display: flex; align-items: center; height: 34px; margin-bottom: 6px;
    font-family: "Montserrat", sans-serif; font-weight: 500; font-size: 15.5px; letter-spacing: 0.6px; color: var(--ink); }
  .service-icon { width: 34px; height: 34px; background: var(--brand-blue); margin-right: 14px; flex: none;
    display: flex; align-items: center; justify-content: center; }

  .side-frame { left: 528px; top: 665px; width: 270px; height: 229px; background: var(--charcoal);
    clip-path: polygon(40% 0, 100% 0, 100% 100%, 0 100%, 2% 96%, 35% 4%); }
  .side-photo { left: 450px; top: 673px; width: 340px; height: 212px;
    background: linear-gradient(180deg, #dfe7ee 0%, #eef1f3 38%, #7ea24a 52%, #8aa95b 66%, #d7cba9 82%, #4b4a45 100%); }

  .values-title { left: 450px; top: 918px; }
  .values-text { left: 450px; top: 952px; width: 340px; font-family: "Jost", sans-serif; font-size: 15px; line-height: 20px; color: var(--ink); }

  .contact-title { left: 450px; top: 1030px; }
  .contact-text { left: 450px; top: 1064px; font-family: "Jost", sans-serif; font-size: 15.5px; line-height: 20px; color: var(--ink); }

  .social { top: 1074px; width: 39px; height: 39px; background: var(--charcoal); }

  .footer-band { left: 13px; top: 1146px; width: 822px; height: 35px; background: var(--brand-blue); }
</style>
</head>
<body>
<div class="flyer">
  <div class="sheet"></div>

  <div class="abs brand">
    <div class="brand-square"></div>
    <div class="brand-name">Tallmere<br>Construction</div>
  </div>
  <div class="abs web">www.<span>tallmereconstruction</span>.com</div>

  <div class="abs hero-band"></div>
  <div class="abs hero-shadow"></div>
  <div class="abs hero-photo" role="img" aria-label="Photo of a completed single-storey brick and white-columned public building with wide concrete entry steps under a blue sky"></div>

  <h2 class="abs section-title services-title"><span class="lead">OUR</span> SERVICES</h2>
  <p class="abs services-intro">Our expertise and technical resources fuel the delivery of our services. As a leading provider of construction services, Tallmere Construction focuses on providing solutions for civil infrastructure, industrial infrastructure, and commercial market segments. Driven by a commitment to continuous improvement, Tallmere Construction has the expertise in the following key areas:</p>

  <ul class="abs service-list">
    <li><span class="service-icon"><svg width="20" height="20" viewBox="0 0 20 20" fill="none" stroke="#fff" stroke-width="1.6"><rect x="3" y="3" width="14" height="14"/><path d="M3 17 17 3"/></svg></span>Design Build/Problem Solving</li>
    <li><span class="service-icon"><svg width="20" height="20" viewBox="0 0 20 20" fill="#fff"><path d="M10 2C7 7 5 9.5 5 12a5 5 0 0 0 10 0c0-2.5-2-5-5-10z"/></svg></span>Storm and Process Water Systems</li>
    <li><span class="service-icon"><svg width="20" height="20" viewBox="0 0 20 20" fill="#fff"><rect x="3" y="11" width="14" height="6"/><rect x="7" y="4" width="6" height="6"/></svg></span>Heavy and Structural Concrete</li>
    <li><span class="service-icon"><svg width="22" height="20" viewBox="0 0 22 20" fill="none" stroke="#fff" stroke-width="1.6"><path d="M1 12h20M2 12q9-10 18 0M5 12v6M11 7v11M17 12v6"/></svg></span>Bridge Construction</li>
    <li><span class="service-icon"><svg width="20" height="20" viewBox="0 0 20 20" fill="none" stroke="#fff" stroke-width="1.6"><rect x="5" y="3" width="10" height="15"/><path d="M8 7h4M8 11h4M8 15h4"/></svg></span>Building Construction and Restoration</li>
    <li><span class="service-icon"><svg width="20" height="20" viewBox="0 0 20 20" fill="none" stroke="#fff" stroke-width="1.5"><rect x="2" y="2" width="7" height="7"/><rect x="11" y="2" width="7" height="7"/><rect x="2" y="11" width="7" height="7"/><rect x="11" y="11" width="7" height="7"/></svg></span>Hardscapes</li>
    <li><span class="service-icon"><svg width="20" height="20" viewBox="0 0 20 20" fill="#fff"><path d="M4 10a6 6 0 0 1 12 0z"/><rect x="3" y="10" width="14" height="2"/><rect x="5" y="14" width="10" height="5"/></svg></span>All Civil Construction and Utility</li>
  </ul>

  <div class="abs side-frame"></div>
  <div class="abs side-photo" role="img" aria-label="Photo of a landscaped campus lawn with young trees, shrubs and a paved walkway"></div>

  <h2 class="abs section-title values-title"><span class="lead">OUR</span> VALUES</h2>
  <p class="abs values-text">Tallmere Construction is committed to excellence. Our core values include delivering high quality, craftsmanship, safety and customer service.</p>

  <h2 class="abs section-title contact-title"><span class="lead">CONTACT</span> US</h2>
  <p class="abs contact-text">820 Foundry Lane<br>Ridgeport, Mississippi 39455<br>601-555-0148</p>

  <div class="abs social" style="left:658px" aria-label="Social profile"></div>
  <div class="abs social" style="left:708px" aria-label="Social profile"></div>
  <div class="abs social" style="left:759px" aria-label="Social profile"></div>

  <div class="abs footer-band"></div>
</div>
</body>
</html>
```